Letterhead & Email Signature Design

Kindly assist redesign this letterhead as well as the Email signature. I have uploaded the current designs that needs some new look

```html
<!DOCTYPE html>
<html lang="en">
<head>
<meta charset="utf-8">
<title>Ndlovu Tau, Inc — Letterhead</title>
<link rel="stylesheet" href="https://fonts.googleapis.com/css2?family=Cormorant+Garamond:wght@500&family=Montserrat:wght@400;600&family=Lora:wght@400&display=swap">
<style>
  :root {
    --backdrop: #e4e4e6;
    --paper: #ffffff;
    --ink: #555557;
    --ink-dark: #2a2a2c;
    --rule-light: #9a9a9c;
    --rule-dark: #5e5e60;
    --accent-bar: #b8b8ba;
  }
  * { box-sizing: border-box; margin: 0; padding: 0; }
  html, body {
    width: 900px; height: 1200px; overflow: hidden;
    background: var(--backdrop);
  }
  .letterhead {
    position: absolute; left: 70px; top: 50px;
    width: 760px; height: 1100px;
    background: var(--paper);
    box-shadow: 0 6px 18px rgba(0,0,0,0.12);
  }
  .brand {
    position: absolute; left: 52px; top: 70px;
    display: flex; align-items: center; gap: 12px;
  }
  .brand-square {
    width: 26px; height: 26px; background: var(--ink);
  }
  .brand-name {
    font-family: "Cormorant Garamond", serif;
    font-weight: 500; font-size: 27px; letter-spacing: 0.5px;
    color: var(--ink);
  }
  .contact {
    position: absolute; left: 440px; top: 60px;
    font-family: "Montserrat", sans-serif; font-size: 10.5px;
    line-height: 15px; color: var(--ink);
  }
  .contact-row { display: flex; align-items: flex-start; gap: 8px; }
  .contact-row svg { flex: none; margin-top: 2px; }
  .contact-phones { display: flex; gap: 40px; }
  .contact-phones span { display: flex; gap: 8px; align-items: center; }
  .header-rule {
    position: absolute; top: 158px; left: 250px; width: 470px; height: 4px;
  }
  .header-rule .thin {
    position: absolute; left: 0; top: 0; width: 260px; height: 1px; background: var(--rule-light);
  }
  .header-rule .thick {
    position: absolute; left: 260px; top: 0; width: 210px; height: 4px; background: var(--rule-dark);
  }
  .letter {
    position: absolute; left: 72px; top: 220px; width: 620px;
    font-family: "Lora", serif; font-size: 13px; line-height: 19px;
    color: var(--ink-dark);
  }
  .letter-date { margin-bottom: 40px; }
  .letter-recipient { margin-bottom: 30px; }
  .letter p { margin-bottom: 18px; text-align: justify; }
  .signature {
    margin-top: 40px; width: 150px; height: 50px;
    background: linear-gradient(90deg, #f2f2f3, #e6e6e8);
  }
  .signatory { margin-top: 6px; }
  .footer-bar {
    position: absolute; left: 58px; bottom: 50px;
    width: 14px; height: 72px; background: var(--accent-bar);
  }
  .footer-web {
    position: absolute; left: 92px; bottom: 62px;
    font-family: "Montserrat", sans-serif; font-weight: 600; font-size: 13px;
    color: var(--ink);
  }
</style>
</head>
<body>
  <main class="letterhead">
    <div class="brand">
      <div class="brand-square"></div>
      <div class="brand-name">NDLOVU TAU, Inc</div>
    </div>

    <div class="contact">
      <div class="contact-row">
        <svg width="10" height="13" viewBox="0 0 10 13"><path d="M5 0C2.2 0 0 2.2 0 4.8 0 8.5 5 13 5 13s5-4.5 5-8.2C10 2.2 7.8 0 5 0zm0 6.7a1.9 1.9 0 1 1 0-3.8 1.9 1.9 0 0 1 0 3.8z" fill="#8a8a8c"/></svg>
        <div>The Willow Office Park | Ground Floor, Building C<br>118 Ridgeview Road | Lynnwood Glen | 0042</div>
      </div>
      <div class="contact-row contact-phones">
        <span><svg width="11" height="11" viewBox="0 0 11 11"><path d="M2.2 0.5l1.6 2.2-1 1.1c.7 1.5 1.9 2.7 3.4 3.4l1.1-1 2.2 1.6-.7 2C5 9.8 1.2 6 .2 1.2z" fill="#8a8a8c"/></svg>Tel: 012 555 0148</span>
        <span><svg width="13" height="11" viewBox="0 0 13 11"><rect x="3" y="0.5" width="7" height="3" fill="none" stroke="#8a8a8c"/><rect x="0.5" y="3.5" width="12" height="7" rx="1" fill="none" stroke="#8a8a8c"/></svg>012 555 0193</span>
      </div>
      <div class="contact-row">
        <svg width="12" height="9" viewBox="0 0 12 9"><rect x="0.5" y="0.5" width="11" height="8" fill="none" stroke="#8a8a8c"/><path d="M0.5 0.5l5.5 4.5 5.5-4.5" fill="none" stroke="#8a8a8c"/></svg>
        <div>info@ndlovutauinc.co.za</div>
      </div>
    </div>

    <div class="header-rule"><div class="thin"></div><div class="thick"></div></div>

    <section class="letter">
      <div class="letter-date">Cartagena de Indias, October 31, 2013</div>
      <div class="letter-recipient">Sr.<br>MARCO RUIZ<br>Web Master<br>City</div>
      <p>Lorem ipsum dolor sit amet,</p>
      <p>Consetetur sadipscing elitr, sed diam nonumy eirmod tempor invidunt ut labore et dolore magna aliquyam erat, sed diam voluptua. At vero eos et accusam et justo duo dolores et ea rebum. Stet clita kasd gubergren, no sea takimata sanctus est. Lorem ipsum dolor sit amet, consetetur sadipscing elitr, sed diam nonumy eirmod tempor invidunt ut labore et dolore magna aliquyam erat, sed diam voluptua.</p>
      <p>Sed diam nonumy eirmod tempor invidunt ut labore et dolore magna aliquyam erat. At vero eos et accusam et justo duo dolores et ea rebum. Stet clita kasd gubergren, no sea takimata sanctus est. Sed diam nonumy eirmod tempor invidunt ut labore et dolore magna aliquyam erat, sed diam voluptua.</p>
      <p>Stet clita kasd gubergren, no sea takimata sanctus est et ea rebum. Lorem ipsum dolor sit amet, eirmod tempor invidunt ut labore, sed diam voluptua.</p>
      <div class="signature" role="img" aria-label="Handwritten signature"></div>
      <div class="signatory">ELENA BROOKS<br>Manager</div>
    </section>

    <div class="footer-bar"></div>
    <div class="footer-web">www.ndlovutauinc.co.za</div>
  </main>
</body>
</html>
```